VELMOR MOBILE APP RE-DESIGN - MINIMALISTIC AND CLEAN DESIGN

We are looking for a design that is minimalistic, clean, modern and appealing to millennials...
IMPORTANT: This is NOT a logo design nor a website design... This is for a mobile App Design. You can download our app on iOS or Android: "VELMOR iLINKUP"

We are attaching our new logo and some apps that we like the design, colors, shadows, 3d effects, style, etc...

For content, you can check our website: www.velmor.example

Please feel free to ask questions, it's very important that you understand the project. Thank you

Also, check out this website...we do like the design and colors: https://brindlo.example/
Updates

This is not for a logo design... this is for a mobile app design.... please download our app on iOS: VELMOR iLINKUP... THANK YOU

Target Market(s)

20 - 35
60% Male 40 Female

Requirements
Must have
• great graphics, color shadows for 3d effects, great colors with transparency, IMPORTANT: CLEAN DESIGN, Minimalistic.

```html
<!DOCTYPE html>
<html lang="en">
<head>
<meta charset="utf-8">
<title>Velmor iLinkup – Account Screens</title>
<link href="https://fonts.googleapis.com/css2?family=Roboto:wght@400;500;700&display=swap" rel="stylesheet">
<style>
:root{
  --bg:#1ac6f5;
  --screen:#f4f6f8;
  --title:#3b4552;
  --text:#2f3742;
  --muted:#6b737d;
  --accent:#1ab4e8;
  --line:#d4d9de;
  --btn-start:#2c4895;
  --btn-end:#1bbaf0;
  --ok:#2fbf71;
  --err:#ef4b5a;
}
*{box-sizing:border-box;margin:0;padding:0}
html,body{width:1200px;height:1200px;overflow:hidden}
body{background:var(--bg);font-family:"Roboto",sans-serif;position:relative;color:var(--text)}
.screen{position:absolute;width:213px;height:460px;border-radius:28px;background:var(--screen);box-shadow:0 14px 30px rgba(10,90,150,.25)}
.screen > *{position:absolute}
.center{left:0;right:0;text-align:center}
.title{font-size:20px;font-weight:700;color:var(--title);line-height:1}
.sub{font-size:8px;color:var(--muted);line-height:14px}
.note{font-size:8px;color:var(--text)}
.note a{color:var(--accent);text-decoration:none;font-weight:500}
.field{left:34px;width:143px;border-bottom:1px solid var(--line)}
.field .label{font-size:8px;color:var(--accent);display:block}
.field .value{font-size:8px;color:var(--text);display:block;margin-top:6px}
.dots{display:flex;gap:4.5px;margin-top:7px}
.dots i{width:9px;height:9px;border-radius:50%;background:#3d4550;display:block}
.field .status{position:absolute;right:0;bottom:8px;width:12px;height:12px}
.btn{left:34px;width:143px;height:28px;border-radius:14px;background:linear-gradient(90deg,var(--btn-start),var(--btn-end));color:#fff;font-size:8.5px;font-weight:500;display:flex;align-items:center;justify-content:center;box-shadow:0 6px 12px rgba(30,120,200,.25)}
.divider{left:34px;width:143px;display:flex;align-items:center;gap:10px;font-size:7px;color:#a7aeb6}
.divider::before,.divider::after{content:"";flex:1;height:1px;background:#cfe6f2}
.social{left:0;right:0;display:flex;justify-content:center;gap:13px}
.social span{width:28px;height:28px;border-radius:50%;background:#fff;box-shadow:0 3px 8px rgba(0,0,0,.08);font-size:5.5px;color:var(--accent);display:flex;align-items:center;justify-content:center;font-weight:500}
.home-bar{left:77px;width:60px;height:3px;border-radius:2px;background:#c9ced4}
.avatar{left:70px;width:72px;height:86px;border-radius:36px 36px 20px 20px;background:linear-gradient(180deg,#f7c6b4 0%,#f2a994 60%,#2fb5e6 100%)}
.otp{left:34px;width:143px;display:flex;justify-content:space-between}
.otp span{width:26px;text-align:center;font-size:8px;border-bottom:1px solid var(--accent);padding-bottom:8px}
.key{left:64px;width:86px;height:86px}
</style>
</head>
<body>

<!-- Register -->
<section class="screen" style="left:85px;top:42px">
  <h1 class="title center" style="top:50px">Register</h1>
  <p class="sub center" style="top:79px">Sign up your velmor account</p>
  <div class="field" style="top:113px;height:37px"><span class="label">Name</span><span class="value">Darin Okafor</span></div>
  <div class="field" style="top:166px;height:37px"><span class="label">Email</span><span class="value">darin.ok@mailbox.example</span></div>
  <div class="field" style="top:219px;height:37px"><span class="label">Password</span>
    <div class="dots"><i></i><i></i><i></i><i></i><i></i><i></i></div>
    <svg class="status" viewBox="0 0 24 24" fill="none" stroke="#1ab4e8" stroke-width="2"><path d="M1 12s4-7 11-7 11 7 11 7-4 7-11 7S1 12 1 12z"/><circle cx="12" cy="12" r="3"/></svg>
  </div>
  <div class="btn" style="top:279px">Register</div>
  <p class="note center" style="top:320px">Already have an account? <a>Login</a></p>
  <div class="divider" style="top:354px">OR</div>
  <p class="note center" style="top:389px">Register with social network</p>
  <div class="social" style="top:412px"><span>Kito</span><span>Plume</span><span>Snapo</span></div>
  <div class="home-bar" style="top:455px"></div>
</section>

<!-- Login -->
<section class="screen" style="left:85px;top:549px">
  <h1 class="title center" style="top:49px">Login</h1>
  <p class="sub center" style="top:79px">Sign in your velmor account</p>
  <div class="field" style="top:115px;height:37px"><span class="label">Email</span><span class="value">darin.ok@mailbox.example</span></div>
  <div class="field" style="top:168px;height:37px"><span class="label">Password</span>
    <div class="dots"><i></i><i></i><i></i><i></i><i></i><i></i></div>
    <svg class="status" viewBox="0 0 24 24" fill="none" stroke="#1ab4e8" stroke-width="2"><path d="M1 12s4-7 11-7 11 7 11 7-4 7-11 7S1 12 1 12z"/><circle cx="12" cy="12" r="3"/></svg>
  </div>
  <p class="note center" style="top:217px">Forgot password? <a style="font-weight:400">Click here</a></p>
  <div class="btn" style="top:247px">Login</div>
  <p class="note center" style="top:288px">Don't have an account? <a>Register</a></p>
  <div class="divider" style="top:323px">OR</div>
  <p class="note center" style="top:357px">Login with social network</p>
  <div class="social" style="top:380px"><span>Kito</span><span>Plume</span><span>Snapo</span></div>
  <div class="home-bar" style="top:453px"></div>
</section>

<!-- Forgot password -->
<section class="screen" style="left:361px;top:380px">
  <h1 class="title center" style="top:50px">Forgot Password</h1>
  <p class="sub center" style="top:79px">Enter your email to receive an<br>OTP to reset password</p>
  <div class="avatar" style="top:151px" role="img" aria-label="Illustration of a worried young man"></div>
  <div class="field" style="top:283px;height:36px"><span class="label">Email</span><span class="value">darin.ok@mailbox.example</span></div>
  <div class="btn" style="top:342px">Send</div>
  <div class="home-bar" style="top:454px"></div>
</section>

<!-- OTP verification -->
<section class="screen" style="left:632px;top:184px">
  <h1 class="title center" style="top:50px">OTP Verification</h1>
  <p class="sub center" style="top:80px">Enter the OTP just sent your email</p>
  <div class="avatar" style="top:152px" role="img" aria-label="Illustration of a smiling young man"></div>
  <div class="otp" style="top:300px"><span>7</span><span>2</span><span>9</span><span>1</span></div>
  <p class="note center" style="top:332px">Didn't receive a OTP ! <a style="font-weight:400">Resend</a></p>
  <div class="btn" style="top:363px">Verify</div>
  <div class="home-bar" style="top:454px"></div>
</section>

<!-- Reset password, matching -->
<section class="screen" style="left:629px;top:691px">
  <h1 class="title center" style="top:49px">Reset Password</h1>
  <p class="sub center" style="top:79px">Enter new password just<br>being extra safe</p>
  <svg class="key" style="top:151px" viewBox="0 0 86 86">
    <circle cx="43" cy="43" r="41" fill="none" stroke="#1ab4e8" stroke-width="1" stroke-dasharray="1.5 3"/>
    <circle cx="2" cy="43" r="2.5" fill="#fff" stroke="#bfe3f3"/>
    <defs><linearGradient id="kg1" x1="0" y1="1" x2="1" y2="0"><stop offset="0" stop-color="#2c4895"/><stop offset="1" stop-color="#1bbaf0"/></linearGradient></defs>
    <circle cx="43" cy="43" r="30" fill="url(#kg1)" stroke="#fff" stroke-width="3"/>
    <circle cx="49" cy="37" r="7" fill="#fff"/><circle cx="51" cy="35" r="2.2" fill="#2a78c4"/>
    <path d="M45 41 L31 55 L34 58 L37 55 L39 57 L42 54 L40 52 L48 44 Z" fill="#fff"/>
  </svg>
  <div class="field" style="top:282px;height:36px"><span class="label">New Password</span>
    <div class="dots"><i></i><i></i><i></i><i></i><i></i><i></i></div>
    <svg class="status" viewBox="0 0 24 24" fill="none" stroke="#1ab4e8" stroke-width="2"><path d="M1 12s4-7 11-7 11 7 11 7-4 7-11 7S1 12 1 12z"/><circle cx="12" cy="12" r="3"/></svg>
  </div>
  <div class="field" style="top:335px;height:36px"><span class="label">Confirm Password</span>
    <div class="dots"><i></i><i></i><i></i><i></i><i></i><i></i></div>
    <svg class="status" viewBox="0 0 24 24" fill="none" stroke="#2fbf71" stroke-width="2"><circle cx="12" cy="12" r="10"/><path d="M7 12l3.5 3.5L17 9"/></svg>
  </div>
  <div class="btn" style="top:394px">Done</div>
  <div class="home-bar" style="top:454px"></div>
</section>

<!-- Reset password, mismatch -->
<section class="screen" style="left:914px;top:503px">
  <h1 class="title center" style="top:49px">Reset Password</h1>
  <p class="sub center" style="top:79px">Enter new password just<br>being extra safe</p>
  <svg class="key" style="top:152px" viewBox="0 0 86 86">
    <circle cx="43" cy="43" r="41" fill="none" stroke="#1ab4e8" stroke-width="1" stroke-dasharray="1.5 3"/>
    <circle cx="2" cy="43" r="2.5" fill="#fff" stroke="#bfe3f3"/>
    <defs><linearGradient id="kg2" x1="0" y1="1" x2="1" y2="0"><stop offset="0" stop-color="#2c4895"/><stop offset="1" stop-color="#1bbaf0"/></linearGradient></defs>
    <circle cx="43" cy="43" r="30" fill="url(#kg2)" stroke="#fff" stroke-width="3"/>
    <circle cx="49" cy="37" r="7" fill="#fff"/><circle cx="51" cy="35" r="2.2" fill="#2a78c4"/>
    <path d="M45 41 L31 55 L34 58 L37 55 L39 57 L42 54 L40 52 L48 44 Z" fill="#fff"/>
  </svg>
  <div class="field" style="top:283px;height:36px"><span class="label">New Password</span>
    <div class="dots"><i></i><i></i><i></i><i></i><i></i><i></i></div>
    <svg class="status" viewBox="0 0 24 24" fill="none" stroke="#1ab4e8" stroke-width="2"><path d="M1 12s4-7 11-7 11 7 11 7-4 7-11 7S1 12 1 12z"/><circle cx="12" cy="12" r="3"/></svg>
  </div>
  <div class="field" style="top:336px;height:36px"><span class="label">Confirm Password</span>
    <div class="dots"><i></i><i></i><i></i><i></i><i></i><i></i></div>
    <svg class="status" viewBox="0 0 24 24" fill="none" stroke="#ef4b5a" stroke-width="2"><path d="M5 5l14 14M19 5L5 19"/></svg>
  </div>
  <div class="btn" style="top:395px">Done</div>
  <div class="home-bar" style="top:454px"></div>
</section>

</body>
</html>
```